Mortgage Protection Insurance Flyer

The target audience are new home owners so the design needs to be clean and simple.

This a primarily for Final Expense Insurance, but need an area where it says "We Also Specialize In:"
- Medicare Supplement Insurance (MediGap)
- Annuities
- Final Expense

All flyer versions need to be editable. Colors to be used are red, white or black. Refer to my website for colors and photos (harborvaleassurance.com). Will attach my logo and a flyer that I found online that is the format that I am looking for (for 8.5 in. x 11 in version). Need flyer in standard letter size 8.5 in. x11 in. but also in 8.5 in. x 5.5 in and 5.0 in. x 8.0 in. All sizes to be portrait oriented. If picked as winning design, need all flyer versions in full color, also in grey scale and files in all industry file types.

Content can be taken from my website..... harborvaleassurance.com

Do NOT submit if you are not willing to provide all versions as described above for the original project price.

Must use royalty-free stock photos please.

Target Market(s)

New homeowners looking for insurance to protect there mortgage payments

Industry/Entity Type

Life Insurance

Colors
f69fa3

Requirements
Must have
• Colors to be used are red, white or black.
• Need flyer in standard letter size 8.5 in. x11 in. but also in 3.5 in. x 8.5 in (Full Bleed 3.75 in by 8.75 in.) and 4.0 in. x 6.0 in. (Full Bleed 4.12 in x 6.12 in) Each design tailored to the size dimensions (So no squeezing 8.5 x 11 design into a 4.0 x 6.0 space.) All sizes to be portrait oriented. If picked as winning design, need all flyer versions in full color, also in grey scale and files in all file types.
• Do not need physical address on flyer, do need email address on flyer though - tkerlow@harborvaleassurance.com
• So phone number should be prominent, email address and website address should also be contact area.
• If you can not agree to terms above, do not submit any designs.
• Need facebook & twitter logos somewhere in contact info area.
Nice to have
• See sample flyers I have attached.
• White background with red used as primary graphic color and black used as secondary graphic if needed.
• font to be used should similar to one used in logo.

```html
<!DOCTYPE html>
<html lang="en">
<head>
<meta charset="utf-8">
<title>Harborvale Assurance – Flyer Set</title>
<link href="https://fonts.googleapis.com/css2?family=Oswald:wght@500;700&family=Open+Sans:wght@400;600&display=swap" rel="stylesheet">
<style>
:root{
  --red:#d42a2a;
  --red-soft:#e0533e;
  --black:#1b1b1b;
  --white:#ffffff;
  --ink:#222222;
  --stage:#e4e4e2;
  --photo-a:#d9c9b2;
  --photo-b:#8e9a52;
}
*{margin:0;padding:0;box-sizing:border-box}
html,body{width:1200px;height:768px;overflow:hidden;background:var(--stage)}
body{position:relative;font-family:"Open Sans",Arial,sans-serif;color:var(--ink)}
.flyer{position:absolute;background:var(--white);overflow:hidden;box-shadow:0 4px 10px rgba(0,0,0,.25)}
.flyer svg.shapes{position:absolute;inset:0}
.flyer .t{position:absolute}
.brand{font-family:"Oswald",Arial,sans-serif;font-weight:700;color:var(--black);letter-spacing:.02em;white-space:nowrap;text-transform:uppercase;line-height:1}
.heading{font-family:"Oswald",Arial,sans-serif;font-weight:500;color:var(--red);text-transform:uppercase;white-space:nowrap;letter-spacing:-.01em}
.rule{position:absolute;height:1px;background:var(--red)}
.copy{line-height:1.4;text-align:justify}
.services{list-style:none}
.services li{position:relative;padding-left:1.5em}
.services li::before{content:"";position:absolute;left:0;top:.35em;width:.8em;height:.8em;border-radius:50%;background:var(--red)}
.contact{list-style:none;color:var(--red)}
.contact li{display:flex;align-items:center;gap:.5em;white-space:nowrap}
.contact .dot{width:1em;height:1em;border-radius:50%;border:1.5px solid var(--black);flex:none}
.social{position:absolute;display:flex;gap:4px}
.social span{display:block;border-radius:50%;background:var(--black)}
.badge{position:absolute;text-align:center;color:var(--white);line-height:1.15}
.badge hr{border:none;height:1px;background:rgba(255,255,255,.35);margin:.5em auto}

/* letter size */
.letter{left:85px;top:82px;width:478px;height:618px}
.letter .copy{font-size:8px}
/* rack card */
.rack{left:621px;top:221px;width:197px;height:476px}
.rack .band{position:absolute;left:0;top:250px;width:197px;height:103px;background:linear-gradient(180deg,#2b2b2b,#151515)}
/* postcard */
.post{left:870px;top:361px;width:224px;height:338px}
</style>
</head>
<body>

<!-- Letter size flyer -->
<section class="flyer letter">
  <svg class="shapes" viewBox="0 0 478 618" width="478" height="618">
    <defs>
      <linearGradient id="photoL" x1="0" y1="0" x2="1" y2="1">
        <stop offset="0" stop-color="var(--photo-a)"/><stop offset="1" stop-color="var(--photo-b)"/>
      </linearGradient>
    </defs>
    <circle cx="35" cy="35" r="82" fill="var(--red-soft)" opacity=".9"/>
    <circle cx="-5" cy="45" r="78" fill="var(--red)"/>
    <circle cx="383" cy="290" r="180" fill="var(--black)"/>
    <circle cx="383" cy="290" r="176" fill="var(--red)"/>
    <circle cx="383" cy="290" r="170" fill="url(#photoL)" role="img" aria-label="Photo of a smiling senior couple embracing"/>
    <circle cx="328" cy="552" r="80" fill="var(--red)"/>
    <circle cx="328" cy="552" r="77" fill="var(--white)"/>
    <circle cx="328" cy="552" r="73" fill="var(--black)"/>
    <circle cx="470" cy="560" r="50" fill="var(--red-soft)"/>
    <circle cx="505" cy="600" r="60" fill="var(--red)"/>
  </svg>
  <div class="t brand" style="right:24px;top:38px;font-size:20px">Harborvale Assurance</div>

  <div class="t heading" style="left:22px;top:116px;font-size:17px">Our plans are based on yours</div>
  <div class="rule" style="left:22px;top:142px;width:170px"></div>
  <p class="t copy" style="left:22px;top:150px;width:178px">Get the right Final Expense Insurance, Medicare Supplement Insurance or Mortgage Protection Insurance plan for your family's peace-of-mind!</p>

  <div class="t heading" style="left:22px;top:218px;font-size:17px">What we specialize in:</div>
  <div class="rule" style="left:22px;top:243px;width:196px"></div>
  <ul class="t services" style="left:22px;top:255px;font-size:10px;line-height:1.65">
    <li>Final Expense Insurance</li>
    <li>Annuities</li>
    <li>Mortgage Protection Insurance</li>
    <li>Medicare Supplement Insurance<br>(MediGap)</li>
  </ul>
  <p class="t" style="left:22px;top:352px;width:188px;font-size:7.5px;line-height:1.5">*Based on an insured that is a 65 year old, non-smoking female that has no medical conditions with death benefit of $2k</p>

  <div class="t heading" style="left:22px;top:404px;font-size:17px">About us:</div>
  <div class="rule" style="left:22px;top:428px;width:196px"></div>
  <p class="t copy" style="left:22px;top:438px;width:218px">We have been helping clients in North Idaho/Eastern Washington prepare for the unknown. We have access to the industry's top insurance carriers so you can get the right coverage that fits your budget.</p>
  <p class="t copy" style="left:22px;top:495px;width:218px">Find out how we can help find the right plan to keep your medical costs manageable.</p>

  <ul class="t contact" style="left:22px;top:553px;font-size:11.5px;line-height:1.55">
    <li><span class="dot"></span>(555)014.2273</li>
    <li><span class="dot"></span>tkerlow@harborvaleassurance.com</li>
    <li><span class="dot"></span>harborvaleassurance.com</li>
  </ul>
  <div class="social" style="left:327px;top:588px"><span style="width:20px;height:20px"></span><span style="width:20px;height:20px"></span></div>

  <div class="badge" style="left:258px;top:505px;width:140px;font-size:13px">
    Monthly premiums<br>as low as $10*<hr style="width:90px">Death Benefits<br>as high as $40,000
  </div>
</section>

<!-- Rack card -->
<section class="flyer rack">
  <svg class="shapes" viewBox="0 0 197 476" width="197" height="476">
    <defs>
      <linearGradient id="photoR" x1="0" y1="0" x2="1" y2="1">
        <stop offset="0" stop-color="var(--photo-a)"/><stop offset="1" stop-color="var(--photo-b)"/>
      </linearGradient>
    </defs>
    <path d="M0 0H197V110Q150 150 100 148Q40 146 0 100Z" fill="url(#photoR)" role="img" aria-label="Photo of a smiling senior couple embracing"/>
    <path d="M0 100Q40 146 100 148Q150 150 197 110" fill="none" stroke="var(--red)" stroke-width="3"/>
    <circle cx="147" cy="154" r="46" fill="var(--red)"/>
    <circle cx="147" cy="154" r="43" fill="var(--white)"/>
    <circle cx="147" cy="154" r="40" fill="var(--black)"/>
    <circle cx="178" cy="455" r="30" fill="var(--red-soft)"/>
    <circle cx="200" cy="480" r="34" fill="var(--red)"/>
  </svg>
  <div class="social" style="left:166px;top:6px"><span style="width:11px;height:11px"></span><span style="width:11px;height:11px"></span></div>
  <div class="badge" style="left:107px;top:134px;width:80px;font-size:7px">
    Monthly premiums<br>as low as $10*<hr style="width:52px;margin:.4em auto">Death Benefits<br>as high as $40,000
  </div>
  <div class="t brand" style="left:10px;top:174px;font-size:8.5px">Harborvale Assurance</div>

  <div class="t heading" style="left:10px;top:204px;font-size:8.5px">Our plans are based on yours</div>
  <p class="t copy" style="left:10px;top:222px;width:180px;font-size:5px">Get the right Final Expense Insurance, Medicare Supplement Insurance or Mortgage Protection Insurance plan for your family's peace-of-mind!</p>

  <div class="band"></div>
  <div class="t heading" style="left:10px;top:257px;font-size:8.5px">What we specialize in:</div>
  <div class="rule" style="left:10px;top:273px;width:96px"></div>
  <ul class="t services" style="left:10px;top:280px;font-size:6.5px;line-height:1.7;color:var(--white)">
    <li>Final Expense Insurance</li>
    <li>Annuities</li>
    <li>Mortgage Protection Insurance</li>
    <li>Medicare Supplement Insurance (MediGap)</li>
  </ul>
  <p class="t" style="left:10px;top:334px;width:180px;font-size:4.6px;line-height:1.45;color:var(--white)">*Based on an insured that is a 65 year old, non-smoking female that has no medical conditions with death benefit of $2k</p>

  <div class="t heading" style="left:10px;top:362px;font-size:8.5px">About us:</div>
  <div class="rule" style="left:10px;top:377px;width:96px"></div>
  <p class="t copy" style="left:10px;top:382px;width:180px;font-size:5px">We have been helping clients in North Idaho/Eastern Washington prepare for the unknown. We have access to the industry's top insurance carriers so you can get the right coverage that fits your budget.</p>
  <p class="t copy" style="left:10px;top:414px;width:180px;font-size:5px">Find out how we can help find the right plan to keep your medical costs manageable.</p>
  <ul class="t contact" style="left:10px;top:441px;font-size:6.5px;line-height:1.6">
    <li><span class="dot"></span>(555)014.2273</li>
    <li><span class="dot"></span>tkerlow@harborvaleassurance.com</li>
    <li><span class="dot"></span>harborvaleassurance.com</li>
  </ul>
</section>

<!-- Postcard -->
<section class="flyer post">
  <svg class="shapes" viewBox="0 0 224 338" width="224" height="338">
    <defs>
      <linearGradient id="photoP" x1="0" y1="0" x2="1" y2="1">
        <stop offset="0" stop-color="var(--photo-a)"/><stop offset="1" stop-color="var(--photo-b)"/>
      </linearGradient>
    </defs>
    <circle cx="20" cy="15" r="40" fill="var(--red-soft)" opacity=".9"/>
    <circle cx="0" cy="22" r="36" fill="var(--red)"/>
    <circle cx="223" cy="170" r="124" fill="var(--black)"/>
    <circle cx="223" cy="170" r="121" fill="var(--red)"/>
    <circle cx="223" cy="170" r="116" fill="url(#photoP)" role="img" aria-label="Photo of a smiling senior couple embracing"/>
    <circle cx="176" cy="240" r="45" fill="var(--red)"/>
    <circle cx="176" cy="240" r="43" fill="var(--white)"/>
    <circle cx="176" cy="240" r="40" fill="var(--black)"/>
    <circle cx="200" cy="325" r="28" fill="var(--red-soft)"/>
    <circle cx="222" cy="345" r="30" fill="var(--red)"/>
  </svg>
  <div class="t brand" style="right:10px;top:20px;font-size:10px">Harborvale Assurance</div>
  <div class="t heading" style="left:8px;top:68px;font-size:7.5px">Our plans are based on yours</div>
  <div class="rule" style="left:8px;top:81px;width:96px"></div>
  <p class="t copy" style="left:8px;top:84px;width:100px;font-size:4.2px">Get the right Final Expense Insurance, Medicare Supplement Insurance or Mortgage Protection Insurance plan for your family's peace-of-mind!</p>

  <div class="t heading" style="left:8px;top:122px;font-size:7.5px">What we specialize in:</div>
  <div class="rule" style="left:8px;top:134px;width:92px"></div>
  <ul class="t services" style="left:8px;top:139px;font-size:5px;line-height:1.75">
    <li>Final Expense Insurance</li>
    <li>Annuities</li>
    <li>Mortgage Protection Insurance</li>
    <li>Medicare Supplement Insurance<br>(MediGap)</li>
  </ul>
  <p class="t" style="left:8px;top:193px;width:92px;font-size:4.2px;line-height:1.45">*Based on an insured that is a 65 year old, non-smoking female that has no medical conditions with death benefit of $2k</p>

  <div class="t heading" style="left:8px;top:222px;font-size:7.5px">About us:</div>
  <div class="rule" style="left:8px;top:234px;width:102px"></div>
  <p class="t copy" style="left:8px;top:238px;width:114px;font-size:4.2px">We have been helping clients in North Idaho/Eastern Washington prepare for the unknown. We have access to the industry's top insurance carriers so you can get the right coverage that fits your budget.</p>
  <p class="t copy" style="left:8px;top:268px;width:114px;font-size:4.2px">Find out how we can help find the right plan to keep your medical costs manageable.</p>

  <ul class="t contact" style="left:8px;top:306px;font-size:5.8px;line-height:1.6">
    <li><span class="dot"></span>(555)014.2273</li>
    <li><span class="dot"></span>tkerlow@harborvaleassurance.com</li>
    <li><span class="dot"></span>harborvaleassurance.com</li>
  </ul>
  <div class="social" style="left:144px;top:317px"><span style="width:11px;height:11px"></span><span style="width:11px;height:11px"></span></div>

  <div class="badge" style="left:136px;top:223px;width:80px;font-size:6.5px">
    Monthly premiums<br>as low as $10*<hr style="width:52px;margin:.4em auto">Death Benefits<br>as high as $40,000
  </div>
</section>

</body>
</html>
```